Packaging Design job - Product : Supplement for Travel Sickness

We need a packaging design for a travel sickness supplement called "VORALIN"

VORALIN It is a dietary supplement based on ginger which has properties fighting against motion sickness.

Ginger is a root used for many years for its beneficial effects on health. In addition to its stimulating and toning properties which help to resist fatigue, ginger is used as an adjuvant in case of nausea, vomiting and motion sickness. Ideal for pregnant women to combat certain disadvantages of pregnancy.

This product will be in blister form of 30 capsules. We need for this a packaging design for the box.Dimensions: 100 * 20 * 200 mm

We would like to see clean, modern and fresh designs.This should give the impression of professional products of pharmaceutical quality. You will also find attached the logo of our company.Ps : You can change the color of the logo

Mention to put on the box :

• Produit en France: Laboratoire CALDOR, 24 Rue des Tilleuls 41120 BRÉVAL
• Distribué au Maroc: KORAVITE 17 rue Idriss Benani 30000 FEZ MAROC
• Complément alimentaire, ce n'est pas un médicament
• Voie orale
• Tenir hors de portée des enfants
• Respectez la dose recommandée
• Ce produit ne remplace pas une alimentation variée

Mode d'utilisation (How to use) :

2 à 3 gélules 30 min avant de prendre le véhicule de transport
1 gélule par jour en cas de cure

Font styles to use
Serif
Sans Serif
Script

Requirements
Should not have
• Sales and other "must buy" "guaranteed" etc

```html
<!DOCTYPE html>
<html lang="fr">
<head>
<meta charset="utf-8">
<title>VORALIN – Dieline de l'étui</title>
<link rel="stylesheet" href="https://fonts.googleapis.com/css2?family=Jost:wght@300;400;600;700;800&family=Arimo:wght@400&display=swap">
<style>
  :root {
    --teal: #1bbbb8;
    --teal-soft: #3fc7c4;
    --grey: #939598;
    --cut: #808080;
    --fold: #e2e2e2;
    --ink: #000000;
    --paper: #ffffff;
  }
  html, body {
    margin: 0;
    padding: 0;
    width: 1200px;
    height: 1132px;
    overflow: hidden;
    background: var(--paper);
  }
  .dieline { display: block; width: 1200px; height: 1132px; }
  .panel-teal { fill: var(--teal); }
  .panel-white { fill: var(--paper); }
  .band-grey { fill: var(--grey); }
  .cut-line { fill: none; stroke: var(--cut); stroke-width: 6; stroke-linejoin: miter; }
  .fold-line { fill: none; stroke: var(--fold); stroke-width: 6; }
  .dim-line { stroke: var(--ink); stroke-width: 6; fill: none; }
  .dim-text { font-family: "Arimo", Arial, sans-serif; font-size: 40px; fill: var(--ink); }
  .product-name { font-family: "Jost", sans-serif; font-weight: 800; fill: var(--paper); letter-spacing: 2px; }
  .product-claim { font-family: "Jost", sans-serif; font-weight: 300; font-size: 30px; fill: var(--paper); }
  .pill-label { font-family: "Jost", sans-serif; font-weight: 700; font-size: 24px; fill: var(--paper); letter-spacing: 1px; }
  .legal-text { font-family: "Jost", sans-serif; font-weight: 400; font-size: 23px; fill: var(--paper); }
  .usage-title { font-family: "Jost", sans-serif; font-weight: 700; font-size: 26px; fill: var(--paper); }
  .brand-name { font-family: "Jost", sans-serif; font-weight: 700; fill: var(--grey); }
  .brand-dot { fill: var(--teal); }
  .ginger-spot { fill: var(--teal-soft); }
  .ginger-disc { fill: var(--paper); }
</style>
</head>
<body>
<svg class="dieline" viewBox="0 0 1975 1880" preserveAspectRatio="none" xmlns="http://www.w3.org/2000/svg">

  <!-- overall dimensions -->
  <g class="dimensions">
    <path class="dim-line" d="M8 125 V72 M8 78 H1835 M1835 72 V125"/>
    <text class="dim-text" x="1015" y="52" text-anchor="middle">268.00mm</text>
    <path class="dim-line" d="M1862 147 H1915 M1910 147 V1867 M1862 1867 H1915"/>
    <text class="dim-text" transform="translate(1935 1060) rotate(90)" text-anchor="middle">252.50mm</text>
  </g>

  <!-- top tuck flap -->
  <path class="cut-line" d="M240 235 L265 147 H1578 L1603 235"/>

  <!-- back panel -->
  <rect class="panel-teal" x="245" y="238" width="1358" height="438"/>
  <rect class="band-grey" x="312" y="682" width="1291" height="12"/>

  <g class="back-copy" transform="rotate(180 924 457)">
    <g class="legal-list">
      <text class="legal-text" x="323" y="307">•&#160;&#160;Produit en France: Laboratoire CALDOR, 24 Rue des Tilleuls 41120 BRÉVAL</text>
      <text class="legal-text" x="323" y="339">•&#160;&#160;Distribué au Maroc: KORAVITE 17 rue Idriss Benani 30000 FEZ MAROC</text>
      <text class="legal-text" x="323" y="374">•&#160;&#160;Complément alimentaire, ce n'est pas un médicament</text>
      <text class="legal-text" x="323" y="406">•&#160;&#160;Voie orale</text>
      <text class="legal-text" x="323" y="438">•&#160;&#160;Tenir hors de portée des enfants</text>
      <text class="legal-text" x="323" y="471">•&#160;&#160;Respectez la dose recommandée</text>
      <text class="legal-text" x="323" y="503">•&#160;&#160;Ce produit ne remplace pas une alimentation variée</text>
    </g>
    <text class="usage-title" x="318" y="553">Mode d'utilisation (How to use)</text>
    <text class="legal-text" x="318" y="597">2 à 3 gélules 30 min avant de prendre le véhicule de transport</text>
    <text class="legal-text" x="318" y="630">1 gélule par jour en cas de cure</text>
    <rect class="ginger-spot" x="1151" y="354" width="282" height="205" rx="90"
          role="img" aria-label="Dessin au trait d'une racine de gingembre avec feuilles"/>
  </g>

  <!-- back logo area -->
  <g class="brand back-brand" transform="rotate(180 629 801)">
    <circle class="brand-dot" cx="452" cy="801" r="26"/>
    <text class="brand-name" x="492" y="828" font-size="76" textLength="340" lengthAdjust="spacingAndGlyphs">KORAVITE</text>
  </g>

  <!-- top side strip -->
  <rect class="panel-teal" x="245" y="918" width="1355" height="130"/>
  <text class="product-name" transform="rotate(180 922 978)" x="922" y="1013" font-size="100" text-anchor="middle">VORALIN</text>

  <!-- fold lines -->
  <path class="fold-line" d="M245 235 H1603 M245 915 H1603 M116 1054 H1603 M116 1732 H1603"/>
  <path class="fold-line" d="M238 1060 V1728 M1605 238 V913 M1733 292 V858 M110 1108 V1676 M1603 1735 V1862"/>

  <!-- front panel -->
  <rect class="panel-white" x="245" y="1060" width="1355" height="215"/>
  <g class="brand front-brand">
    <circle class="brand-dot" cx="1170" cy="1166" r="28"/>
    <text class="brand-name" x="1212" y="1195" font-size="80" textLength="338" lengthAdjust="spacingAndGlyphs">KORAVITE</text>
  </g>
  <rect class="band-grey" x="116" y="1275" width="119" height="12"/>
  <rect class="band-grey" x="243" y="1275" width="1357" height="12"/>

  <rect class="panel-teal" x="116" y="1293" width="119" height="435"/>
  <rect class="panel-teal" x="243" y="1293" width="1357" height="435"/>

  <text class="product-name" x="312" y="1448" font-size="156" textLength="665" lengthAdjust="spacingAndGlyphs">VORALIN</text>
  <text class="product-claim" x="315" y="1496">VORALIN It is a dietary supplement based on ginger which</text>
  <text class="product-claim" x="315" y="1530">has properties fighting against motion sickness.</text>

  <rect class="band-grey" x="315" y="1572" width="198" height="60" rx="30"/>
  <text class="pill-label" x="414" y="1610" text-anchor="middle">30 CAPSULES</text>

  <circle class="ginger-disc" cx="1330" cy="1480" r="155"
          role="img" aria-label="Illustration au trait d'une racine de gingembre et de ses feuilles dans un disque blanc"/>

  <!-- bottom side strip -->
  <rect class="panel-teal" x="245" y="1737" width="1355" height="125"/>
  <text class="product-name" x="922" y="1833" font-size="100" text-anchor="middle">VORALIN</text>

  <!-- cut outline -->
  <path class="cut-line" d="M240 235 V918 M240 1052 V1865 M1603 235 V1865"/>
  <path class="cut-line" d="M200 1865 H1718"/>

  <!-- right tuck flap -->
  <path class="cut-line" d="M1603 235 H1737 V290 H1732 M1732 860 H1737 V913 H1603"/>
  <path class="cut-line" d="M1737 237 C1790 237 1835 275 1835 305 V848 C1810 890 1780 913 1737 913"/>

  <!-- dust flaps -->
  <path class="cut-line" d="M1603 918 H1718 V1015 L1665 1028 L1642 1048 H1603"/>
  <path class="cut-line" d="M240 918 H200 L180 940 L125 955 V1048 H240"/>
  <path class="cut-line" d="M240 1735 H125 V1830 L180 1845 L200 1865"/>
  <path class="cut-line" d="M1603 1735 H1642 L1665 1757 L1718 1770 V1865"/>

  <!-- left tuck flap -->
  <path class="cut-line" d="M240 1052 H105 V1108 H110 M110 1676 H105 V1730 H240"/>
  <path class="cut-line" d="M105 1055 C55 1055 8 1095 8 1120 V1660 C20 1700 55 1728 105 1730"/>

  <!-- panel dimensions -->
  <g class="dimensions">
    <path class="dim-line" d="M310 238 V913 M310 913 V1052"/>
    <path d="M310 236 l-8 16 h16 z M310 911 l-8 -16 h16 z M310 915 l-8 16 h16 z M310 1054 l-8 -16 h16 z" fill="#000"/>
    <text class="dim-text" transform="translate(338 655) rotate(90)" text-anchor="middle">100.00mm</text>
    <text class="dim-text" transform="translate(338 1062) rotate(90)" text-anchor="middle">20.00mm</text>
    <path class="dim-line" d="M240 1665 H1605"/>
    <path d="M238 1665 l16 -8 v16 z M1607 1665 l-16 -8 v16 z" fill="#000"/>
    <text class="dim-text" x="990" y="1638" text-anchor="middle">200.00mm</text>
  </g>
</svg>
</body>
</html>
```